Fundraising Study Day East of England. Lift the January blues!

A flyer to advertise a fundraising event of lectures for dental hygienists and therapists in support of the exemption campaign. Currently dental hygienists and therapists require a prescription to deliver certain treatment or recommend certain toothpastes. If we are successful in the campaign we will be able to treat patients without these restrictions.

Industry/Entity Type

Dental

```html
<!DOCTYPE html>
<html lang="en">
<head>
<meta charset="utf-8">
<title>Lift the January Blues – Fundraising Study Day</title>
<link href="https://fonts.googleapis.com/css2?family=Lato:wght@400;700;900&display=swap" rel="stylesheet">
<style>
  :root {
    --bg: #e9e9ea;
    --paper: #f1f1f2;
    --ink: #1d1b1c;
    --red: #e3141e;
    --blue: #25288f;
    --rule: #3a3d9a;
    --white: #ffffff;
    --wash-warm: rgba(240, 170, 120, .22);
    --wash-cool: rgba(150, 140, 210, .22);
  }
  * { margin: 0; padding: 0; box-sizing: border-box; }
  html, body { width: 1200px; height: 906px; overflow: hidden; }
  body {
    background: var(--bg);
    font-family: "Lato", sans-serif;
    color: var(--ink);
    display: flex; align-items: center; justify-content: center;
  }
  .flyer {
    position: relative;
    width: 620px; height: 872px;
    background: var(--paper);
    overflow: hidden;
    box-shadow: 0 2px 10px rgba(0,0,0,.12);
  }
  .artwork {
    position: absolute; left: 30px; top: 300px; width: 560px; height: 400px;
    background: linear-gradient(160deg, var(--wash-warm), var(--wash-cool));
  }
  .header { position: relative; padding: 26px 30px 0; }
  .kicker { color: var(--red); font-weight: 900; font-size: 27px; letter-spacing: .2px; }
  .headline { color: var(--blue); font-weight: 900; font-size: 44px; line-height: 1.05; margin-top: 2px; }
  .intro { font-size: 13.5px; line-height: 1.3; margin-top: 10px; text-align: justify; }
  .info { position: relative; height: 170px; margin-top: 14px; }
  .tag {
    position: absolute; background: var(--ink); color: var(--white);
    border-radius: 0 0 16px 0; padding: 8px 14px; font-size: 14px; line-height: 1.2;
  }
  .tag b { font-weight: 900; font-size: 16px; display: block; letter-spacing: .5px; }
  .tag--location { left: 0; top: 0; width: 200px; }
  .tag--location .venue { font-weight: 700; }
  .tag--date { left: 230px; top: 40px; width: 170px; }
  .tag--cost { right: 0; top: 70px; width: 170px; height: 80px; text-align: center; font-size: 22px; border-radius: 0 0 0 16px; }
  .tag--cost b { font-size: 24px; }
  .agenda-title {
    position: absolute; left: 230px; top: 120px; color: var(--blue);
    font-weight: 900; font-size: 38px; line-height: 1; letter-spacing: 1px;
  }
  .agenda { position: relative; display: flex; gap: 28px; padding: 0 30px; margin-top: 4px; }
  .agenda__col { flex: 1; }
  .slot { border-bottom: 2px solid var(--rule); padding: 8px 0 10px; font-size: 13.5px; line-height: 1.3; }
  .slot--last { border-bottom: 0; }
  .slot__time { font-weight: 900; font-size: 18px; display: block; }
  .slot strong { font-weight: 900; }
  .closing { position: relative; padding: 14px 30px 0; font-size: 13.5px; line-height: 1.3; }
  .closing strong { font-weight: 900; }
  .footer {
    position: absolute; left: 0; right: 0; bottom: 0; height: 86px;
    background: var(--ink); color: var(--white);
    display: flex; align-items: center; justify-content: center; text-align: center;
    font-weight: 700; font-size: 15px; line-height: 1.35; padding: 0 30px;
  }
</style>
</head>
<body>
  <main class="flyer">
    <div class="artwork" role="img" aria-label="Area for colourful painted handprints artwork"></div>

    <header class="header">
      <p class="kicker">Fundraising Study Day East of England</p>
      <h1 class="headline">LIFT THE JANUARY BLUES!</h1>
      <p class="intro">A fundraising event to support our exemptions project. The day will consist of a series of presentations ranging from the new ECPD to new technologies. The aim, being to enhance our learning and raise funds to support the exemptions campaign. The speaker line includes some of the UK and Irelands most respected dental professionals in our field.</p>
    </header>

    <section class="info">
      <div class="tag tag--location"><b>LOCATION</b><span class="venue">Larchmont Hotel</span><br>Orbit Lane, Hatfield,<br>AL10 4QZ</div>
      <div class="tag tag--date"><b>DATE &amp; TIME</b>Fri 19 January 2018<br>09:00 – 16:30 GMT</div>
      <h2 class="agenda-title">AGENDA</h2>
      <div class="tag tag--cost"><b>Cost</b>£101.48</div>
    </section>

    <section class="agenda">
      <div class="agenda__col">
        <p class="slot"><span class="slot__time">9.30 - 10.15</span><strong>Helen Marsh:</strong> Immediate past president of the HTG will be updating us on all things ECPD</p>
        <p class="slot"><span class="slot__time">10.15 - 11.00</span><strong>Rachel Dunmore:</strong> Will provide an update on teeth whitening and explain how social media has impacted her business</p>
        <p class="slot"><strong>Clara Whitfield:</strong> Our internationally acclaimed speaker will update our knowledge of periodontal disease and nutrition and new technologies.</p>
        <p class="slot"><span class="slot__time">11.00 - 11.30 Break</span></p>
      </div>
      <div class="agenda__col">
        <p class="slot"><span class="slot__time">11.30 - 13.00</span><strong>Niamh Carroway &amp; Dana Ellery:</strong> Will be providing a combined presentation on 'Scaling your business' and start to finish Sonara techniques. The aim being to build our business with effective communications, systems and protocols. This sessions promises audience participation!</p>
        <p class="slot"><span class="slot__time">12 - 1400 Lunch</span></p>
        <p class="slot"><span class="slot__time">14 - 15.00</span><strong>Priya Lal:</strong> Save your back. All things posture.</p>
        <p class="slot"><span class="slot__time">15.00 - 15.30 Break</span></p>
        <p class="slot slot--last"><span class="slot__time">15.30 - 16.30</span></p>
      </div>
    </section>

    <p class="closing"><strong>Clara Whitfield:</strong> Our internationally acclaimed speaker will update our knowledge of periodontal disease and nutrition and new technologies</p>

    <footer class="footer">https://www.ticketdesk.co.uk/e/fundraising-study-day-east-of-england-<br>lift-the-january-blues-tickets-40215573108</footer>
  </main>
</body>
</html>
```